" A empresa opera inteiramente o segmento de tecnologia e pesquisa, focando no desenvolvimento de soluções únicas e disruptivas, com portifólio próprio de sistemas. "

```html
<!DOCTYPE html>
<html lang="pt-BR">
<head>
<meta charset="utf-8">
<title>NOVUX — Crachás</title>
<link rel="stylesheet" href="https://fonts.googleapis.com/css2?family=Montserrat:wght@400;500;600;700&display=swap">
<style>
  :root {
    --bg: #4b4b4b;
    --card-dark: #3f3f3f;
    --card-light: #ffffff;
    --ink-light: #ffffff;
    --ink-dark: #3a3a3a;
    --ink-muted: #8a8a8a;
    --field: #efefef;
    --hole: #2e2e2e;
  }
  * { box-sizing: border-box; margin: 0; padding: 0; }
  html, body { width: 1200px; height: 1200px; overflow: hidden; }
  body {
    background: var(--bg);
    font-family: "Montserrat", sans-serif;
    position: relative;
  }
  .badge {
    position: absolute;
    top: 330px;
    width: 340px;
    height: 540px;
    border-radius: 22px;
    overflow: hidden;
  }
  .badge-hole {
    position: absolute;
    top: 30px; left: 50%;
    width: 22px; height: 22px;
    margin-left: -11px;
    border-radius: 50%;
    background: var(--hole);
  }
  /* front */
  .badge-front { left: 230px; background: var(--card-dark); color: var(--ink-light); }
  .badge-front .badge-hole { background: #2a2a2a; }
  .portrait {
    position: absolute;
    left: 86px; top: 130px;
    width: 170px; height: 221px;
    background: linear-gradient(180deg, #e9e9ea 0%, #d9c3b5 60%, #c9a792 100%);
  }
  .brand {
    position: absolute;
    display: flex; align-items: center; gap: 10px;
  }
  .brand-mark { width: 18px; height: 18px; background: currentColor; }
  .brand-name { font-weight: 700; font-size: 30px; letter-spacing: 2px; line-height: 1; }
  .brand-tagline { font-size: 7px; line-height: 1.25; font-weight: 500; width: 80px; opacity: .85; }
  .badge-front .brand { left: 42px; top: 392px; }
  .holder-name {
    position: absolute; left: 0; right: 0; top: 458px;
    text-align: center; font-weight: 600; font-size: 21px; letter-spacing: .5px;
  }
  .holder-role {
    position: absolute; left: 0; right: 0; top: 494px;
    text-align: center; font-weight: 500; font-size: 14px;
  }
  /* back */
  .badge-back { left: 630px; background: var(--card-light); color: var(--ink-dark); }
  .badge-back .brand { left: 80px; top: 86px; }
  .badge-back .brand-name { font-size: 27px; }
  .badge-back .brand-tagline { color: var(--ink-muted); }
  .field { position: absolute; left: 34px; right: 34px; }
  .field-label { font-size: 11px; font-weight: 500; color: var(--ink-dark); }
  .field-bar { margin-top: 6px; margin-left: 70px; height: 26px; background: var(--field); }
  .contacts {
    position: absolute; left: 70px; right: 30px; top: 436px;
    display: grid; grid-template-columns: 1fr 1.3fr; row-gap: 16px; column-gap: 8px;
    font-size: 11px; color: var(--ink-dark);
  }
  .contact { display: flex; align-items: center; gap: 6px; white-space: nowrap; }
  .contact svg { width: 13px; height: 13px; flex: none; }
</style>
</head>
<body>
  <section class="badge badge-front">
    <span class="badge-hole"></span>
    <div class="portrait" role="img" aria-label="Foto de retrato da colaboradora"></div>
    <div class="brand">
      <span class="brand-mark"></span>
      <span class="brand-name">NOVUX</span>
      <span class="brand-tagline">Sistemas e pesquisa em tecnologia</span>
    </div>
    <p class="holder-name">Marina Castro</p>
    <p class="holder-role">Diretora Geral</p>
  </section>

  <section class="badge badge-back">
    <span class="badge-hole"></span>
    <div class="brand">
      <span class="brand-mark"></span>
      <span class="brand-name">NOVUX</span>
      <span class="brand-tagline">Sistemas e pesquisa em tecnologia</span>
    </div>
    <div class="field" style="top:180px"><p class="field-label">nome completo</p><div class="field-bar"></div></div>
    <div class="field" style="top:250px"><p class="field-label">cargo</p><div class="field-bar"></div></div>
    <div class="field" style="top:318px"><p class="field-label">rg</p><div class="field-bar"></div></div>
    <div class="contacts">
      <span class="contact"><svg viewBox="0 0 14 14"><circle cx="7" cy="7" r="6" fill="none" stroke="#777" stroke-width="1.2"/></svg>@novux</span>
      <span class="contact"><svg viewBox="0 0 14 14"><circle cx="7" cy="7" r="6" fill="none" stroke="#777" stroke-width="1.2"/><path d="M1 7h12M7 1c3 3 3 9 0 12M7 1c-3 3-3 9 0 12" fill="none" stroke="#777" stroke-width="1"/></svg>novux.com</span>
      <span class="contact"><svg viewBox="0 0 14 14"><path d="M3 1.5l2.5 2.5-1.3 1.6c.8 1.7 2.1 3 3.8 3.8L9.6 8l2.9 2.5-1.4 2c-5 0-9.6-4.6-9.6-9.6z" fill="#777"/></svg>21 90000-1234</span>
      <span class="contact"><svg viewBox="0 0 14 14"><rect x="1" y="3" width="12" height="8" fill="none" stroke="#777" stroke-width="1.2"/><path d="M1 3l6 5 6-5" fill="none" stroke="#777" stroke-width="1.2"/></svg>contato@novux.com</span>
    </div>
  </section>
</body>
</html>
```